Business Cards for IT Consulting Company (Managed Service Provider)

I am looking to have some business cards printed and would like some designs. We are an IT Consulting company based in Vancouver BC. I would like a nice clean and modern look to the cards. I have uploaded all the versions of my logo so parts can be used as needed. Here is a snippit from our website homepage:

Kelbrin Systems Ltd. is an IT Solutions Partner located in Vancouver BC, Canada. We offer IT solutions and support to customers in the greater Vancouver Area. With expertise in Quillara platforms, as well as Tovex and Bryn ZPL and over 12 years experience in the IT industry, Kelbrin Systems is dedicated to offering our clients top quality service and products. We take pride in the solutions we offer our customers. The greatest compliment a client can give us is to recommend our services.

Kelbrin Systems Ltd. offers a wide range of IT services from onsite service to remote support and managed service solutions. This allows clients to choose the support path that best suits their company’s needs. Supporting many different sized companies from small to enterprise level over the past 12 years Kelbrin Systems has the experience and expertise needed to ensure things run smoothly. Allowing our clients to focus on doing business.

Revolutionizing the way IT services are delivered.

Kelbrin Systems is dedicated to providing our clients with IT solutions that work and grow with them for years to come. This philosophy helps save money in the long run instead of replacing equipment constantly. Far too often IT solutions are not well thought out and while possibly solving the problem at hand, require replacement due to growth or quality within a very short time frame. Kelbrin Systems takes pride in providing solutions that will last and be able to accommodate growth without the need for replacement.

Industry/Entity Type

Information Technology

Contact Information for Business Card

Kelbrin Systems Ltd.
(Employee Name)
Eml: (Employees Email Address)
Web: kelbrinsys.me
Ph: 604-555-0142

Font styles to use
Serif
Sans Serif

Requirements
Must have
• The Company logo and company colors.
Nice to have
• - Our tag line: "Revolutionizing IT Services" or "Revolutionizing the way IT services are delivered."
• - Also I really like the idea of nature and technology together blending which is sort of where my logo came from so integrating that somehow onto the business cards would be great.

```html
<!DOCTYPE html>
<html lang="en">
<head>
<meta charset="utf-8">
<title>Kelbrin Systems Ltd. – Business Card</title>
<link rel="stylesheet" href="https://fonts.googleapis.com/css2?family=Montserrat:wght@500;600&family=Open+Sans:wght@400&display=swap">
<style>
  :root {
    --backdrop: #d8d5d1;
    --card: #eef1f3;
    --card-edge: #c9cfd4;
    --name-blue: #1b8ed6;
    --brand-blue: #1a6ea8;
    --icon-blue: #1f7fc4;
    --symbol-tint: #cfe0ee;
    --text-dark: #3a3f44;
  }
  * { margin: 0; padding: 0; box-sizing: border-box; }
  html, body {
    width: 1200px;
    height: 969px;
    overflow: hidden;
    background: var(--backdrop);
  }
  .business-card {
    position: absolute;
    left: 100px;
    top: 201px;
    width: 1000px;
    height: 567px;
    background: var(--card);
    border: 1px solid var(--card-edge);
    box-shadow: 0 10px 30px rgba(0, 0, 0, 0.12);
    overflow: hidden;
  }
  .contact-block {
    position: absolute;
    left: 55px;
    top: 135px;
    font-family: "Open Sans", Arial, sans-serif;
    color: var(--text-dark);
  }
  .person-name {
    font-family: "Montserrat", Arial, sans-serif;
    font-weight: 600;
    font-size: 38px;
    line-height: 1;
    color: var(--name-blue);
    margin-bottom: 34px;
  }
  .address {
    font-size: 24px;
    line-height: 29px;
    margin-bottom: 14px;
  }
  .contact-list {
    list-style: none;
  }
  .contact-item {
    display: flex;
    align-items: center;
    gap: 12px;
    font-size: 24px;
    line-height: 38px;
  }
  .contact-icon {
    width: 22px;
    height: 22px;
    flex: none;
  }
  .company-name {
    position: absolute;
    left: 55px;
    top: 425px;
    font-family: "Montserrat", Arial, sans-serif;
    font-weight: 600;
    font-size: 44px;
    line-height: 1;
    color: var(--brand-blue);
  }
  .brand-symbol-area {
    position: absolute;
    left: 476px;
    top: 36px;
    width: 480px;
    height: 480px;
    border-radius: 50%;
    background: var(--symbol-tint);
  }
</style>
</head>
<body>
  <main class="business-card">
    <section class="contact-block">
      <h1 class="person-name">Dara Whitlow</h1>
      <p class="address">4120 Larchmere Road<br>Kodiak Bay, Alaska 30918</p>
      <ul class="contact-list">
        <li class="contact-item">
          <svg class="contact-icon" viewBox="0 0 24 24" aria-hidden="true">
            <path fill="var(--icon-blue)" d="M6.6 10.8a15.1 15.1 0 0 0 6.6 6.6l2.2-2.2a1 1 0 0 1 1-.25 11.4 11.4 0 0 0 3.6.57 1 1 0 0 1 1 1V20a1 1 0 0 1-1 1A17 17 0 0 1 3 4a1 1 0 0 1 1-1h3.5a1 1 0 0 1 1 1c0 1.25.2 2.45.57 3.6a1 1 0 0 1-.25 1z"/>
          </svg>
          <span>604-555-0142</span>
        </li>
        <li class="contact-item">
          <svg class="contact-icon" viewBox="0 0 24 24" aria-hidden="true">
            <rect x="2" y="5" width="20" height="14" rx="1.5" fill="var(--icon-blue)"/>
            <path d="M3 6.5l9 6.5 9-6.5" fill="none" stroke="var(--card)" stroke-width="1.8"/>
          </svg>
          <span>dwhitlow@kelbrinsys.me</span>
        </li>
        <li class="contact-item">
          <svg class="contact-icon" viewBox="0 0 24 24" aria-hidden="true">
            <circle cx="12" cy="12" r="10" fill="var(--icon-blue)"/>
            <path d="M2 12h20M12 2c3 3 3 17 0 20M12 2c-3 3-3 17 0 20" fill="none" stroke="var(--card)" stroke-width="1.4"/>
          </svg>
          <span>www.kelbrinsys.me</span>
        </li>
      </ul>
    </section>
    <p class="company-name">Kelbrin Systems Ltd.</p>
    <div class="brand-symbol-area" role="img" aria-label="Area for the Kelbrin Systems brand symbol in company blue"></div>
  </main>
</body>
</html>
```